依頼詳細
パッケージは、台紙にブリスターケース。
台紙サイズ縦155mm×横90mm
容器は、左下に設置します。
容器サイズは、93mm×横19mm
ブランド名、MIRETO 商品名、KOSEFU for Menは必ず入れてください。
キャッチコピー…出来る男の花粉対策という文字を入れてください。
記載項目
写真はフォトリンデルの№38261507の男性を使ってください
※すでに契約しています
希望イメージ
シンプル 複雑
単色 カラフル
暗い 明るい
日常 高級
遊び心 厳粛
未来的 伝統的
女性的 男性的
希望する色
納品ファイル
• 高解像度JPG (.jpg)
• イラストレーター形式 (.ai)
補足説明
販売価格が1500円前後。買いやすい設定にしています。男性が気軽に手に取れるパッケージをお願いします。
写真は、添付したものをご使用ください。(契約済み)

```html
<!DOCTYPE html>
<html lang="ja">
<head>
<meta charset="utf-8">
<title>KOSEFU for Men パッケージデザイン提案</title>
<link rel="stylesheet" href="https://fonts.googleapis.com/css2?family=Oswald:wght@700&family=Noto+Sans+JP:wght@500;900&display=swap">
<style>
  :root {
    --page: #ffffff;
    --rule: #9a9a9a;
    --ink: #333333;
    --card-dark: #3a3636;
    --card-edge: #2a2727;
    --accent-red: #d8262c;
    --white: #ffffff;
    --tile-ink: #1c1a1a;
    --warm-bg: #c9c4bd;
    --warm-skin: #a88f7d;
    --warm-scarf: #6e6a66;
    --warm-glove: #1f1d1d;
    --mono-bg: #d2d2d2;
    --mono-skin: #9a9a9a;
    --mono-scarf: #6a6a6a;
    --mono-glove: #1c1c1c;
  }
  * { box-sizing: border-box; margin: 0; padding: 0; }
  html, body { width: 846px; height: 1200px; overflow: hidden; background: var(--page); }
  body { position: relative; font-family: "Noto Sans JP", sans-serif; color: var(--ink); }

  .sheet-frame {
    position: absolute; left: 14px; top: 28px; width: 818px; height: 1144px;
    border: 1px solid var(--rule);
  }
  .sheet-header {
    position: absolute; left: 14px; top: 28px; width: 818px; height: 34px;
    border-bottom: 1px solid var(--rule);
    font-size: 12px; font-weight: 500; line-height: 34px; padding-left: 8px;
  }
  .variant-label { position: absolute; top: 244px; font-size: 13px; font-weight: 500; }

  .package {
    position: absolute; top: 282px; width: 362px; height: 620px;
    background: var(--card-dark); border-radius: 14px; overflow: hidden;
    border: 1px solid var(--card-edge);
  }
  .package--a1 { left: 46px; }
  .package--a2 { left: 440px; }

  .hang-hole {
    position: absolute; left: 166px; top: 14px; width: 30px; height: 30px;
    border-radius: 50%; background: var(--page);
  }
  .product-photo { position: absolute; left: 0; top: 92px; width: 362px; height: 446px; }
  .package--a1 .product-photo {
    background:
      radial-gradient(ellipse 90px 150px at 200px 330px, var(--warm-glove) 0%, rgba(31,29,29,0.85) 55%, rgba(31,29,29,0) 100%),
      radial-gradient(ellipse 120px 130px at 200px 150px, var(--warm-skin) 0%, rgba(168,143,125,0.6) 55%, rgba(168,143,125,0) 100%),
      radial-gradient(ellipse 190px 170px at 190px 360px, var(--warm-scarf) 0%, rgba(110,106,102,0) 100%),
      linear-gradient(180deg, var(--warm-bg) 0%, #a9a49e 60%, #5d5a57 100%);
  }
  .package--a2 .product-photo {
    background:
      radial-gradient(ellipse 90px 150px at 200px 330px, var(--mono-glove) 0%, rgba(28,28,28,0.85) 55%, rgba(28,28,28,0) 100%),
      radial-gradient(ellipse 120px 130px at 200px 150px, var(--mono-skin) 0%, rgba(154,154,154,0.6) 55%, rgba(154,154,154,0) 100%),
      radial-gradient(ellipse 190px 170px at 190px 360px, var(--mono-scarf) 0%, rgba(106,106,106,0) 100%),
      linear-gradient(180deg, var(--mono-bg) 0%, #a8a8a8 60%, #555555 100%);
  }
  .product-name {
    position: absolute; left: 0; top: 42px; width: 362px; text-align: center;
    font-family: "Oswald", sans-serif; font-weight: 700; font-size: 80px;
    letter-spacing: 3px; line-height: 84px; color: var(--white);
  }
  .product-sub {
    position: absolute; left: 16px; top: 136px;
    font-family: "Oswald", sans-serif; font-weight: 700; font-size: 32px; line-height: 40px;
  }
  .package--a1 .product-sub { color: var(--accent-red); }
  .package--a2 .product-sub { color: var(--white); }

  .blister-window { position: absolute; left: 6px; width: 36px; }
  .package--a1 .blister-window { top: 146px; height: 392px; background: rgba(205, 214, 222, 0.55); }
  .package--a2 .blister-window { top: 172px; height: 366px; background: var(--white); }

  .tagline-lead {
    position: absolute; left: 96px; top: 392px;
    font-weight: 900; font-size: 32px; line-height: 42px; color: var(--white);
  }
  .tagline-main { position: absolute; left: 96px; top: 440px; display: flex; gap: 6px; }
  .tagline-main span {
    display: block; width: 60px; height: 64px; background: var(--white);
    color: var(--tile-ink); font-weight: 900; font-size: 50px; line-height: 64px; text-align: center;
  }
  .brand-band {
    position: absolute; left: 0; bottom: 0; width: 362px; height: 82px; background: var(--card-dark);
  }
  .brand-name {
    position: absolute; left: 0; bottom: 24px; width: 362px; text-align: center;
    font-family: "Oswald", sans-serif; font-weight: 700; font-size: 28px; line-height: 34px;
    letter-spacing: 2px; color: var(--white);
  }
</style>
</head>
<body>
  <div class="sheet-frame"></div>
  <div class="sheet-header">「KOSEFU for Men」パッケージデザイン提案</div>

  <div class="variant-label" style="left:46px">A-1</div>
  <div class="variant-label" style="left:440px">A-2</div>

  <section class="package package--a1">
    <div class="product-photo" role="img" aria-label="Colour photo of a man in a grey knit scarf and dark gloves holding a tissue to his nose"></div>
    <div class="blister-window"></div>
    <div class="hang-hole"></div>
    <h1 class="product-name">KOSEFU</h1>
    <p class="product-sub">for Men</p>
    <p class="tagline-lead">出来る男の</p>
    <p class="tagline-main"><span>花</span><span>粉</span><span>対</span><span>策</span></p>
    <div class="brand-band"></div>
    <p class="brand-name">MIRETO</p>
  </section>

  <section class="package package--a2">
    <div class="product-photo" role="img" aria-label="Black and white photo of a man in a knit scarf and dark gloves holding a tissue to his nose"></div>
    <div class="blister-window"></div>
    <div class="hang-hole"></div>
    <h1 class="product-name">KOSEFU</h1>
    <p class="product-sub">for Men</p>
    <p class="tagline-lead">出来る男の</p>
    <p class="tagline-main"><span>花</span><span>粉</span><span>対</span><span>策</span></p>
    <div class="brand-band"></div>
    <p class="brand-name">MIRETO</p>
  </section>
</body>
</html>
```